BRIGHTDESK COWORKING Website design and coding

BRIGHTDESK COWORKING

BRIGHTDESK is Galveston’s first (and currently only) shared business co-working space. We share the same upscale, casual work environment, but we work independently on our own (or our team’s) projects and goals. For only a flat $195 membership fee per month, you have your very own all-inclusive, fun, personal business office environment. Website is written (Word file #12, below); and all pictures etc provided. Galveston is a beachy, coastal, historic city an hour from Houston, Texas USA. Logo (file 11 below) is temporary only.

Target Market(s)

Outside sales people, medical students looking for study hall, Houston companies looking for local office, real estate agents, graphic artists, entrepreneurs, etc

Contact Information for Business Card

will discuss --want to combine with current business card with multiple businesses

Logo Text

BRIGHTDESK COWORKING

Coding

Coded - Design and coding required

Number of Pages Required

5+ page

Colors
ec1f27
fbed22

Requirements
Nice to have
• maroon/wine dominant with yellow and red accents, gray base are the colors of the space--website could coordinate--but open to creative ideas/combinations

```html
<!DOCTYPE html>
<html lang="en">
<head>
<meta charset="utf-8">
<title>BRIGHTDESK COWORKING</title>
<link href="https://fonts.googleapis.com/css2?family=Roboto:wght@300;400;500;700;900&display=swap" rel="stylesheet">
<style>
:root{
  --red:#ec1f27;
  --yellow:#fbed22;
  --dark:#2b2b2b;
  --darker:#1f1f1f;
  --ink:#111;
  --text:#555;
  --white:#fff;
}
*{box-sizing:border-box;margin:0;padding:0}
html,body{width:1200px;height:4458px;overflow:hidden}
body{font-family:'Roboto',sans-serif;color:var(--ink);background:var(--white);position:relative}
section,header,footer{position:relative;width:1200px;overflow:hidden}
.abs{position:absolute}
.btn{position:absolute;display:flex;align-items:center;justify-content:center;border-radius:30px;font-weight:700;font-size:15px;letter-spacing:1px}
.btn-yellow{background:var(--yellow);color:var(--ink)}
.btn-red{background:var(--red);color:var(--white)}
.btn-dark{background:#222;color:var(--white)}

/* header */
.site-header{height:107px;background:#fff}
.logo{left:62px;top:20px;text-align:center}
.logo-name{font-size:34px;font-weight:900;letter-spacing:-.5px;line-height:1}
.logo-sub{font-size:23px;font-weight:300;color:var(--red);line-height:1.1}
.main-nav{left:296px;top:43px;display:flex;gap:34px;font-size:13px;color:#444}
.header-phone{right:34px;top:40px;font-size:16px;font-weight:700;display:flex;align-items:center;gap:6px}

/* hero */
.hero{height:646px}
.hero-tint{left:0;top:0;width:606px;height:646px;background:linear-gradient(180deg,#ee2a2e 0%,#f4631f 40%,#f7b81d 75%,#f9e222 100%)}
.hero-photo{left:606px;top:0;width:594px;height:646px;background:linear-gradient(160deg,#9a8a6a 0%,#4b3f33 45%,#1d1a18 100%)}
.hero-title{left:0;width:618px;top:190px;text-align:center;color:#fff;font-weight:900;font-size:58px;line-height:60px}
.hero-sub{left:0;width:618px;top:322px;text-align:center;color:#fff;font-weight:300;font-size:29px}
.hero-arrow{top:278px;width:36px;height:60px;background:var(--red);display:flex;align-items:center;justify-content:center}

/* about */
.about{height:589px}
.about-photo{left:111px;top:62px;width:444px;height:444px;border-radius:50%;background:linear-gradient(150deg,#c9c6bf 0%,#7a7873 45%,#2d2c2b 100%)}
.section-title{font-weight:700;color:var(--ink)}
.about-title{left:608px;top:105px;font-size:33px;line-height:42px;font-weight:500}
.underline{height:3px;width:68px;background:var(--red)}
.about-text{left:608px;top:228px;width:462px;font-size:13px;line-height:27px;color:var(--text)}

/* amenities */
.amenities{height:571px;background:linear-gradient(180deg,#353535 0%,#1d1d1d 100%);color:#fff}
.amenities-title{width:1200px;top:68px;text-align:center;font-size:34px;font-weight:700}
.amenities-intro{left:280px;width:640px;top:128px;text-align:center;font-size:16px;line-height:25px;color:#ddd}
.amenity{display:flex;align-items:center;gap:12px;font-size:12.5px;line-height:17px;color:#fff}
.amenity svg{flex:none}

/* philosophy */
.philosophy{height:601px}
.philosophy-title{width:1200px;top:70px;text-align:center;font-size:34px}
.card{top:163px;width:236px;height:312px;border:2px solid #e3e3e3;box-shadow:0 0 6px rgba(0,0,0,.08);text-align:center;padding:0 24px}
.card svg{margin-top:16px}
.card h3{font-size:15px;font-weight:700;line-height:19px;margin-top:10px}
.card p{font-size:11px;line-height:19px;color:var(--text);margin-top:12px}

/* membership */
.membership{height:617px;background:var(--red)}
.membership-photo{left:0;top:0;width:1200px;height:617px;background:linear-gradient(160deg,#8c8170 0%,#4e3d33 45%,#1c1715 100%);clip-path:polygon(701px 0,1200px 0,1200px 617px,429px 617px)}
.membership-corner{left:0;top:0;width:1200px;height:617px;background:var(--yellow);clip-path:polygon(0 584px,455px 556px,429px 617px,0 617px)}
.membership-title{left:109px;top:166px;font-size:34px;color:#fff;font-weight:700}
.membership-text{left:112px;top:250px;width:430px;font-size:12.5px;line-height:23px;color:#fff}

/* gallery */
.gallery{height:673px;background:var(--yellow)}
.gallery-title{width:1200px;top:63px;text-align:center;font-size:34px}
.shot{background:linear-gradient(150deg,#9b9282,#4b4239 55%,#221d1a)}

/* contact */
.contact{height:450px;background:linear-gradient(180deg,#303030 0%,#222 100%);color:#fff}
.contact-title{width:1200px;top:75px;text-align:center;font-size:34px;color:#fff;font-weight:700}
.contact-col{top:190px;width:250px;text-align:center;font-size:18px;line-height:29px}
.contact-col strong{font-weight:500;display:block}
.contact-col svg{margin:0 auto 18px;display:block}
.divider{top:198px;width:1px;height:148px;background:#777}

/* footer */
.site-footer{height:204px;background:var(--red);color:#fff}
.footer-nav{width:1200px;top:56px;display:flex;justify-content:center;gap:42px;font-size:13px;font-weight:500}
.copyright{width:1200px;top:92px;text-align:center;font-size:11px}
.social{top:136px;display:flex;gap:8px;left:558px}
.social span{width:30px;height:30px;border-radius:50%;background:var(--yellow);display:block}
</style>
</head>
<body>

<header class="site-header">
  <div class="logo abs">
    <div class="logo-name">BRIGHTDESK</div>
    <div class="logo-sub">COWORKING</div>
  </div>
  <nav class="main-nav abs">
    <span>ABOUT</span><span>AMENITIES</span><span>MEMBERSHIP</span><span>PICTURES</span><span>THE BRIGHTDESK PHILOSOPHY</span><span>CONTACT</span>
  </nav>
  <div class="header-phone abs">
    <svg width="16" height="16" viewBox="0 0 24 24"><path fill="#ec1f27" d="M6.6 10.8a15 15 0 0 0 6.6 6.6l2.2-2.2a1 1 0 0 1 1-.25 11.4 11.4 0 0 0 3.6.57 1 1 0 0 1 1 1V20a1 1 0 0 1-1 1A17 17 0 0 1 3 4a1 1 0 0 1 1-1h3.5a1 1 0 0 1 1 1c0 1.25.2 2.45.57 3.57a1 1 0 0 1-.25 1z"/></svg>
    713-555-0148
  </div>
</header>

<section class="hero">
  <div class="hero-tint abs" role="img" aria-label="Lounge of the coworking space with a red to yellow colour wash"></div>
  <div class="hero-photo abs" role="img" aria-label="Lounge with black leather sofa, glass office doors and kitchen bar"></div>
  <h1 class="hero-title abs">BRIGHTDESK<br>COWORKING</h1>
  <div class="hero-sub abs">BUSINESS CO-WORKING SPACE</div>
  <div class="btn btn-dark" style="left:206px;top:378px;width:210px;height:56px;font-size:17px">PLAY NOW</div>
  <div class="hero-arrow abs" style="left:0"><svg width="14" height="24" viewBox="0 0 14 24"><path d="M12 2 2 12l10 10" stroke="#fff" stroke-width="2" fill="none"/></svg></div>
  <div class="hero-arrow abs" style="right:0"><svg width="14" height="24" viewBox="0 0 14 24"><path d="M2 2l10 10L2 22" stroke="#fff" stroke-width="2" fill="none"/></svg></div>
</section>

<section class="about">
  <div class="about-photo abs" role="img" aria-label="Lounge with white sectional sofa, lockers and yellow gaming chair"></div>
  <h2 class="about-title abs section-title">ABOUT<br>BRIGHTDESK COWORKING</h2>
  <div class="underline abs" style="left:608px;top:194px"></div>
  <p class="about-text abs">BRIGHTDESK is Galveston’s first (and currently only) shared business co-working space. We share the same upscale, casual work environment, but we work independently on our own (or our team’s) projects and goals. For only a flat $195 membership fee per month, you have your very own all-inclusive, fun, personal business office environment.</p>
  <div class="btn btn-yellow" style="left:604px;top:390px;width:202px;height:52px">LEARN MORE</div>
</section>

<section class="amenities">
  <h2 class="amenities-title abs">AMENITIES</h2>
  <p class="amenities-intro abs">BRIGHTDESK is the first Galveston co-working space, and offers all of the following features, all included in your monthly $195 membership fee:</p>

  <div class="amenity abs" style="left:160px;top:252px"><svg width="42" height="38" viewBox="0 0 42 38" fill="none" stroke="#fff" stroke-width="2"><rect x="2" y="4" width="38" height="18"/><rect x="14" y="8" width="14" height="10"/><path d="M6 22v14M36 22v14M18 28h6"/></svg><span>Open office or a<br>private cubicle for<br>your daily use.</span></div>
  <div class="amenity abs" style="left:395px;top:256px"><svg width="42" height="34" viewBox="0 0 42 34" fill="none" stroke="#fff" stroke-width="2.5"><path d="M3 12a26 26 0 0 1 36 0M9 18a17 17 0 0 1 24 0M15 24a8 8 0 0 1 12 0"/><circle cx="21" cy="30" r="2" fill="#fff"/></svg><span>24 hour access<br>&amp; Free WiFi</span></div>
  <div class="amenity abs" style="left:615px;top:254px"><svg width="48" height="40" viewBox="0 0 48 40" fill="none" stroke="#fff" stroke-width="2"><rect x="16" y="2" width="16" height="10"/><path d="M4 24h40M8 24v14M40 24v14"/><circle cx="14" cy="18" r="3"/><circle cx="34" cy="18" r="3"/></svg><span>Private conference<br>rooms for meetings</span></div>
  <div class="amenity abs" style="left:878px;top:252px"><svg width="40" height="42" viewBox="0 0 40 42" fill="none" stroke="#fff" stroke-width="2"><rect x="4" y="2" width="22" height="38"/><rect x="26" y="14" width="10" height="26"/><path d="M9 8h4M17 8h4M9 15h4M17 15h4M9 22h4M17 22h4M9 29h4M17 29h4"/></svg><span>Building is a fabulous example<br>of Mid-Century</span></div>

  <div class="amenity abs" style="left:160px;top:338px"><svg width="42" height="30" viewBox="0 0 42 30" fill="none" stroke="#fff" stroke-width="2"><rect x="2" y="10" width="38" height="18"/><rect x="8" y="14" width="10" height="10"/><path d="M24 16h10M24 22h10M10 10V4h6"/></svg><span>Communal coffee<br>bar and kitchen,<br>with FREE coffee</span></div>
  <div class="amenity abs" style="left:395px;top:340px"><svg width="40" height="34" viewBox="0 0 40 34" fill="none" stroke="#fff" stroke-width="2"><circle cx="12" cy="9" r="5"/><circle cx="28" cy="9" r="5"/><path d="M2 32a10 10 0 0 1 20 0M18 32a10 10 0 0 1 20 0"/></svg><span>Great opportunity<br>for networking or<br>mentoring</span></div>
  <div class="amenity abs" style="left:612px;top:342px"><svg width="54" height="28" viewBox="0 0 54 28" fill="none" stroke="#fff" stroke-width="2"><rect x="2" y="6" width="50" height="20"/><path d="M2 12h50M14 12v14M40 12v14M22 2h10v4"/></svg><span>Kitchen and bar area, with<br>commercial sink</span></div>
  <div class="amenity abs" style="left:872px;top:334px"><svg width="48" height="44" viewBox="0 0 48 44" fill="none" stroke="#fff" stroke-width="2"><path d="M10 30a8 8 0 0 1 2-15 11 11 0 0 1 21-2 8 8 0 0 1 4 15z"/><circle cx="8" cy="38" r="3"/><circle cx="40" cy="6" r="3"/><circle cx="42" cy="38" r="2"/></svg><span>Nightly ozone hospital grade<br>disinfection</span></div>

  <div class="btn btn-yellow" style="left:504px;top:455px;width:186px;height:50px">LEARN MORE</div>
</section>

<section class="philosophy">
  <h2 class="philosophy-title abs section-title">THE BRIGHTDESK PHILOSOPHY</h2>
  <div class="underline abs" style="left:566px;top:118px"></div>

  <div class="card abs" style="left:116px">
    <svg width="96" height="96" viewBox="0 0 96 96"><rect x="20" y="20" width="56" height="56" rx="10" transform="rotate(45 48 48)" fill="#fbed22"/><g fill="none" stroke="#ec1f27" stroke-width="2.5"><path d="M30 44h36M34 44v22M62 44v22M42 44v12h12V44M46 30h4v8h-4z"/></g></svg>
    <h3>WORK OUTSIDE<br>THE HOME</h3>
    <p>BRIGHTDESK is the first Galveston co-working space, and offers all of the following features, all included in your monthly $195 membership fee:</p>
  </div>
  <div class="card abs" style="left:364px">
    <svg width="96" height="96" viewBox="0 0 96 96"><rect x="20" y="20" width="56" height="56" rx="10" transform="rotate(45 48 48)" fill="#fbed22"/><g fill="none" stroke="#ec1f27" stroke-width="2.5"><path d="M32 52h32M36 52v12M60 52v12"/><circle cx="38" cy="40" r="4"/><circle cx="58" cy="40" r="4"/><path d="M30 52l4-6h8M66 52l-4-6h-8"/></g></svg>
    <h3>WORK IT OUT WITH<br>YOUR COWORKERS</h3>
    <p>BRIGHTDESK is a community – if you are making a pot of (free) coffee – ask and make enough for everyone that wants some!</p>
  </div>
  <div class="card abs" style="left:611px">
    <svg width="96" height="96" viewBox="0 0 96 96"><rect x="20" y="20" width="56" height="56" rx="10" transform="rotate(45 48 48)" fill="#fbed22"/><g fill="none" stroke="#ec1f27" stroke-width="2.5"><path d="M40 28h16v10a8 8 0 0 1-16 0zM48 46v8M40 54h16v10H40zM36 64h24"/></g></svg>
    <h3>BRIGHTDESK THE<br>COMPETITION</h3>
    <p>Because of the flexibility, prestigious location, opportunities to meet and network with active professionals, and the available tech</p>
  </div>
  <div class="card abs" style="left:857px">
    <svg width="96" height="96" viewBox="0 0 96 96"><rect x="20" y="20" width="56" height="56" rx="10" transform="rotate(45 48 48)" fill="#fbed22"/><g fill="none" stroke="#ec1f27" stroke-width="2.5"><circle cx="60" cy="32" r="5"/><path d="M60 37c0 10-24 4-24 14s20 4 20 10-14 6-20 6"/><circle cx="34" cy="62" r="3" fill="#ec1f27"/></g></svg>
    <h3>WORK OUT THE PATH<br>TO YOUR SUCCESS</h3>
    <p>As your business grows, there are other beautiful, “dedicated desk” private executive offices, and full office suites available in the building</p>
  </div>

  <div class="btn btn-red" style="left:514px;top:508px;width:174px;height:44px;font-size:13px">LEARN MORE</div>
</section>

<section class="membership">
  <div class="membership-photo abs" role="img" aria-label="Kitchen bar with stools, pendant lamps and wine-coloured bar front"></div>
  <div class="membership-corner abs"></div>
  <h2 class="membership-title abs">MEMBERSHIP</h2>
  <div class="underline abs" style="left:112px;top:220px;background:var(--yellow)"></div>
  <p class="membership-text abs">For only $195 a month, charged to your credit card, you get the all-inclusive amenities listed above, for one flat fee. The only “extras” are for copies, on a per-copy basis. WiFi, coffee, use of the conference room, office use, use of the kitchen and all the other features listed under “AMENITIES” above, are INCLUDED at no additional cost.</p>
  <div class="btn btn-yellow" style="left:112px;top:393px;width:184px;height:48px;font-size:14px">LEARN MORE</div>
</section>

<section class="gallery">
  <h2 class="gallery-title abs section-title">OUR GALLERY</h2>
  <div class="underline abs" style="left:550px;top:116px;background:#222"></div>
  <div class="shot abs" style="left:116px;top:154px;width:462px;height:216px" role="img" aria-label="Open work area with lockers, sofa and wooden desks"></div>
  <div class="shot abs" style="left:589px;top:154px;width:462px;height:216px" role="img" aria-label="Yellow and black gaming chairs by a glass wall"></div>
  <div class="shot abs" style="left:116px;top:386px;width:303px;height:203px" role="img" aria-label="Row of desks with lamps by a window"></div>
  <div class="shot abs" style="left:431px;top:386px;width:303px;height:203px" role="img" aria-label="Glass doorway into the conference room"></div>
  <div class="shot abs" style="left:748px;top:386px;width:303px;height:203px" role="img" aria-label="Kitchen with steel fridge and bar counter"></div>
</section>

<section class="contact">
  <h2 class="contact-title abs">CONTACT US</h2>
  <div class="underline abs" style="left:566px;top:128px;background:var(--yellow)"></div>

  <div class="contact-col abs" style="left:77px">
    <svg width="42" height="42" viewBox="0 0 42 42"><circle cx="21" cy="21" r="21" fill="#fbed22"/><rect x="11" y="14" width="20" height="14" fill="none" stroke="#ec1f27" stroke-width="2"/><path d="M11 14l10 8 10-8" fill="none" stroke="#ec1f27" stroke-width="2"/></svg>
    <strong>Harbor Lane Interests</strong>hello@harborlanepc.com
  </div>
  <div class="divider abs" style="left:348px"></div>
  <div class="contact-col abs" style="left:329px;top:183px">
    <svg width="42" height="42" viewBox="0 0 42 42"><circle cx="21" cy="21" r="21" fill="#fbed22"/><path fill="#ec1f27" d="M15 18.5a13 13 0 0 0 8.5 8.5l2.6-2.6a1 1 0 0 1 1-.2 9 9 0 0 0 2.9.5.9.9 0 0 1 .9.9v3.5a.9.9 0 0 1-.9.9A15.5 15.5 0 0 1 12 12.1a.9.9 0 0 1 .9-.9h3.5a.9.9 0 0 1 .9.9c0 1 .2 2 .5 2.9a1 1 0 0 1-.2 1z"/></svg>
    <strong>Phone Number</strong>713-555-0148
  </div>
  <div class="divider abs" style="left:580px"></div>
  <div class="contact-col abs" style="left:581px">
    <svg width="42" height="42" viewBox="0 0 42 42"><circle cx="21" cy="21" r="21" fill="#fbed22"/><path d="M21 10a7 7 0 0 0-7 7c0 5 7 14 7 14s7-9 7-14a7 7 0 0 0-7-7z" fill="#ec1f27"/><circle cx="21" cy="17" r="2.6" fill="#fbed22"/></svg>
    <strong>BRIGHTDESK Coworking</strong>418 Seawall Row, Suite 101<br>Galveston, TX 77550
  </div>
  <div class="divider abs" style="left:832px"></div>
  <div class="contact-col abs" style="left:846px">
    <svg width="42" height="42" viewBox="0 0 42 42"><circle cx="21" cy="21" r="21" fill="#fbed22"/><path d="M21 10a7 7 0 0 0-7 7c0 5 7 14 7 14s7-9 7-14a7 7 0 0 0-7-7z" fill="#ec1f27"/><circle cx="21" cy="17" r="2.6" fill="#fbed22"/></svg>
    <strong>Mailing address</strong>905 Bayou Ave., Suite 200<br>Houston, TX 77002
  </div>
</section>

<footer class="site-footer">
  <nav class="footer-nav abs">
    <span>HOME</span><span>ABOUT</span><span>AMENITIES</span><span>MEMBERSHIP</span><span>PICTURES</span><span>THE BRIGHTDESK PHILOSOPHY</span><span>CONTACT</span>
  </nav>
  <div class="copyright abs">Copyright © 2020 BRIGHTDESK Coworking &nbsp;|&nbsp; Privacy Policy</div>
  <div class="social abs"><span></span><span></span><span></span></div>
</footer>

</body>
</html>
```